Web design for a Crane & Heavy Equipment Inspection, Repair and Maintenance Company in Texas

We need a web design for a new company based in Houston, Texas called "Kelder Crane & Equipment". We inspect, repair and maintain diesel driven heavy equipment, generators, fire water pumps and cranes. We would like to see designs that use the colors orange, white, yellow and brown, and/or orange, white, navy, yellow and grey.

```html
<!DOCTYPE html>
<html lang="en">
<head>
<meta charset="utf-8">
<title>Kelder Crane &amp; Equipment</title>
<link href="https://fonts.googleapis.com/css2?family=Questrial&family=Open+Sans:wght@400;600&family=Orbitron:wght@700&display=swap" rel="stylesheet">
<style>
:root{
  --navy:#143f6e;
  --navy-deep:#0f3561;
  --orange:#f57a16;
  --orange-light:#ff9633;
  --yellow:#f4e21d;
  --grey-text:#8a8a8a;
  --body-text:#555;
  --line:#d8d8d8;
  --page:#ffffff;
}
*{margin:0;padding:0;box-sizing:border-box}
html,body{width:1063px;height:1200px;overflow:hidden;background:var(--page)}
body{position:relative;font-family:"Open Sans",Arial,sans-serif;color:var(--body-text)}
.abs{position:absolute}

.site-header{left:0;top:0;width:1063px;height:102px;background:var(--navy)}
.brand{left:147px;top:40px;font-family:"Questrial",sans-serif;font-size:29px;line-height:1;color:#fff;letter-spacing:.5px;display:flex;align-items:center;gap:8px}
.brand-mark{width:14px;height:14px;background:var(--orange)}
.contact-label{right:148px;top:47px;font-family:"Questrial",sans-serif;font-size:12px;color:#fff}
.contact-phone{right:148px;top:64px;display:flex;align-items:center;gap:6px;font-family:"Questrial",sans-serif;font-size:21px;color:var(--yellow)}

.nav-band{left:0;top:102px;width:1063px;height:45px;background:repeating-linear-gradient(135deg,#f77c18 0 3px,#fb8b2a 3px 6px)}
.main-nav{left:140px;top:102px;width:790px;height:45px;display:flex;background:linear-gradient(#ff8a22,#f26a08);list-style:none}
.main-nav li{height:45px;display:flex;align-items:center;justify-content:center;font-family:"Questrial",sans-serif;font-size:14px;color:#fff;border-right:1px solid rgba(255,255,255,.22)}
.main-nav li:last-child{border-right:none}
.main-nav li.active{background:var(--navy-deep)}
.dropdown{left:691px;top:147px;width:165px;background:var(--navy-deep);list-style:none;padding:6px 0 7px}
.dropdown li{height:23px;line-height:23px;padding-left:27px;font-size:10.5px;color:#fff;border-bottom:1px solid rgba(255,255,255,.12)}
.dropdown li:last-child{border-bottom:none}

.hero-bg{left:0;top:147px;width:1063px;height:362px;background:repeating-linear-gradient(135deg,#f1f1f1 0 2px,#e8e8e8 2px 4px)}
.hero-photo{left:140px;top:147px;width:790px;height:362px;background:linear-gradient(180deg,#dfe6ee 0%,#eef1f4 40%,#d7b43a 62%,#6b6e63 85%,#3d4238 100%)}
.hero-caption{left:173px;top:283px;width:362px;height:111px;background:repeating-linear-gradient(135deg,rgba(24,52,120,.93) 0 2px,rgba(30,62,138,.93) 2px 4px);padding:20px 0 0 28px}
.hero-title{font-family:"Orbitron",sans-serif;font-weight:700;font-size:19.5px;line-height:29px;color:var(--yellow);letter-spacing:.5px}
.hero-title .light{color:#fff8b0}
.hero-sub{margin-top:3px;font-family:"Questrial",sans-serif;font-size:12.5px;color:#fff}
.slider-dots{left:512px;top:491px;display:flex;gap:3px}
.slider-dots span{width:10px;height:10px;border-radius:50%;background:#fff}

.service{width:188px}
.service-photo{width:188px;height:94px}
.service h3{margin-top:12px;font-family:"Questrial",sans-serif;font-weight:400;font-size:15px;color:var(--navy)}
.service p{margin-top:3px;font-size:10px;line-height:17px;color:var(--grey-text)}
.btn{display:inline-block;margin-top:9px;width:82px;height:23px;line-height:23px;text-align:center;background:var(--orange);color:#fff;font-size:8px;font-weight:600}

.welcome{left:145px;top:773px;width:502px}
.welcome h1{font-family:"Questrial",sans-serif;font-weight:400;font-size:20px;color:var(--navy)}
.welcome p{margin-top:9px;font-size:10.6px;line-height:19px;color:var(--body-text)}
.welcome h2{margin-top:15px;font-family:"Questrial",sans-serif;font-weight:400;font-size:13.5px;color:#555}
.diff{top:938px;width:173px;text-align:center}
.diff svg{display:block;margin:0 auto}
.diff h3{font-family:"Questrial",sans-serif;font-weight:400;font-size:14px;color:var(--orange);margin-top:6px}
.diff p{font-size:9.5px;line-height:16px;color:var(--grey-text)}
.diff-divider{top:938px;width:1px;height:105px;background:var(--line)}

.leaders{left:698px;top:773px;width:232px}
.leaders h2{font-family:"Questrial",sans-serif;font-weight:400;font-size:17.5px;color:#444}
.leader{padding:9px 0 10px;border-bottom:1px solid var(--line);width:222px}
.leader:last-child{border-bottom:none}
.leader h3{font-weight:400;font-size:11px;color:var(--orange)}
.leader p{margin-top:5px;font-size:9.5px;line-height:14px;color:#777;width:232px}

.footer-rule{left:0;top:1107px;width:1063px;height:1px;background:var(--line)}
.footer{left:0;top:1108px;width:1063px;height:92px;background:#fbfbfb}
.footer-nav{left:143px;top:1130px;font-family:"Questrial",sans-serif;font-size:12.5px;color:#333;word-spacing:1px}
.copyright{left:144px;top:1158px;font-size:10px;color:var(--grey-text)}
.social{top:1135px;width:20px;height:20px}
</style>
</head>
<body>

<header class="site-header abs">
  <div class="brand abs"><span class="brand-mark"></span>Kelder Crane &amp; Equipment</div>
  <div class="contact-label abs">Contact Us</div>
  <div class="contact-phone abs">
    <svg width="22" height="22" viewBox="0 0 22 22" aria-hidden="true"><circle cx="11" cy="11" r="10" fill="none" stroke="#fff" stroke-width="1.6"/><path d="M7.5 6.5c.8-.6 1.6-.3 2 .5l.6 1.3c.3.6 0 1.1-.5 1.5.6 1.3 1.5 2.3 2.7 3 .4-.5 1-.8 1.6-.5l1.2.7c.8.4 1 1.3.4 2-1 1-2.3 1.2-3.8.3-2.3-1.3-4.3-3.6-5-5.9-.4-1.3 0-2.3.8-2.9z" fill="#fff"/></svg>
    555.204.3170
  </div>
</header>

<div class="nav-band abs"></div>
<ul class="main-nav abs">
  <li style="width:104px">HOME</li>
  <li style="width:119px">ABOUT US</li>
  <li style="width:114px">SERVICES</li>
  <li style="width:98px">REPAIR</li>
  <li style="width:118px">SUPPORT</li>
  <li class="active" style="width:109px">CLIENTS</li>
  <li style="width:128px">CONTACT</li>
</ul>

<div class="hero-bg abs"></div>
<div class="hero-photo abs" role="img" aria-label="Large yellow mobile crane on a job site under a cloudy sky"></div>
<div class="hero-caption abs">
  <div class="hero-title">REPAIR DIESEL DIVEN<br><span class="light">HEAVY EQUIPMENT</span></div>
  <div class="hero-sub">PHASELLUS FELIS DOLOR SCELERISQUE</div>
</div>
<div class="slider-dots abs"><span></span><span></span><span></span><span></span></div>

<ul class="dropdown abs">
  <li>Mauris vel lacus</li>
  <li>Vitae felis vestibu</li>
  <li>Etiam est nunc</li>
  <li>Venenatis in trist</li>
  <li>Imperdiet ac nisl</li>
  <li>Cum sociis natoque</li>
</ul>

<section class="service abs" style="left:139px;top:523px">
  <div class="service-photo" role="img" aria-label="Technician in a hard hat repairing a generator engine" style="background:linear-gradient(90deg,#c9b48e,#8c7a60 55%,#2c3a55)"></div>
  <h3>Generators Repairing</h3>
  <p>Etiam est nunc venenatis in tristique eu imperdiet ac nisl Cum sociis</p>
  <span class="btn">LEARN MORE</span>
</section>
<section class="service abs" style="left:340px;top:523px">
  <div class="service-photo" role="img" aria-label="Inspectors in hard hats checking a crane cab" style="background:linear-gradient(90deg,#5f93c8,#d6d9dc 45%,#e3b52a)"></div>
  <h3>Inspect Diesel Equipment</h3>
  <p>Etiam est nunc venenatis in tristique eu imperdiet ac nisl Cum sociis</p>
  <span class="btn">LEARN MORE</span>
</section>
<section class="service abs" style="left:541px;top:523px">
  <div class="service-photo" role="img" aria-label="Red fire water pump and control panel" style="background:linear-gradient(90deg,#c9c9c9,#b5352e 40%,#d84a3c 80%,#c8c8c8)"></div>
  <h3>Fire Water Pumps</h3>
  <p>Etiam est nunc venenatis in tristique eu imperdiet ac nisl Cum sociis</p>
  <span class="btn">LEARN MORE</span>
</section>
<section class="service abs" style="left:741px;top:523px">
  <div class="service-photo" role="img" aria-label="Mechanic servicing crane machinery" style="background:linear-gradient(90deg,#3c4350,#6c7686 55%,#2f8ed6)"></div>
  <h3>Maintenance Cranes</h3>
  <p>Etiam est nunc venenatis in tristique eu imperdiet ac nisl Cum sociis</p>
  <span class="btn">LEARN MORE</span>
</section>

<section class="welcome abs">
  <h1>WELCOME TO KELDER CRANE &amp; EQUIPMENTS</h1>
  <p>Kelder Crane and Equipment Services Company, LLC provides on-site crane, generator and heavy equip-ment repair, maintenance and inspection.&nbsp; Our commitment to our clients extends beyond our core values of safety, honesty, quality and reliability.&nbsp; We are leveraging technology to improve our clients’ access to inspection, maintenance and repair records.</p>
  <h2>Key differentiators are:</h2>
</section>

<div class="diff abs" style="left:131px">
  <svg width="36" height="36" viewBox="0 0 36 36" aria-hidden="true"><g fill="var(--orange)"><path d="M6 30l17-17 3 3-17 17z"/><path d="M20 4l12 12-4 4-12-12z"/><path d="M6 6a6 6 0 0 0 7 8l16 16 3-3-16-16a6 6 0 0 0-8-7l4 4-2 2z"/></g></svg>
  <h3>Safety</h3>
  <p>Job Safety Analysis is completed<br>on site, on-line - every time</p>
</div>
<div class="diff-divider abs" style="left:304px"></div>
<div class="diff abs" style="left:304px">
  <svg width="36" height="36" viewBox="0 0 36 36" aria-hidden="true"><g fill="var(--orange)"><path d="M12 8h12v4H12z"/><circle cx="18" cy="14" r="6"/><path d="M6 34c0-8 5-13 12-13s12 5 12 13z"/><path d="M29 4h3v6h-1v14h-1V10h-1z"/></g></svg>
  <h3>Technicians</h3>
  <p>Job Safety Analysis is completed<br>on site, on-line - every time</p>
</div>
<div class="diff-divider abs" style="left:477px"></div>
<div class="diff abs" style="left:484px;top:934px">
  <svg width="44" height="36" viewBox="0 0 44 36" aria-hidden="true"><g fill="var(--orange)"><circle cx="14" cy="11" r="7"/><circle cx="30" cy="11" r="7"/><path d="M2 32c0-8 5-13 12-13s12 5 12 13z"/><path d="M18 32c0-8 5-13 12-13s12 5 12 13z"/></g></svg>
  <h3>Contracted clients</h3>
  <p>Job Safety Analysis is completed<br>on site, on-line - every time</p>
</div>

<aside class="leaders abs">
  <h2>Company leaders</h2>
  <div class="leader">
    <h3>Dana Marlow, President</h3>
    <p>a Top 200 corporate sales leader, with 20 years’ experience in sales and management of multi-million dollar corporate accounts</p>
  </div>
  <div class="leader">
    <h3>Curtis Marlow, General Manager</h3>
    <p>a disabled veteran and former Department of Defense Electronic Commerce expert with 20 years’ experience in Information Technology.</p>
  </div>
  <div class="leader">
    <h3>Ray Tollefsen,</h3>
    <p>Field Service Manager - a 15 year Houston area expert in the crane and heavy equipment service industry.</p>
  </div>
</aside>

<div class="footer abs"></div>
<div class="footer-rule abs"></div>
<nav class="footer-nav abs">Home&nbsp; | &nbsp;About Us&nbsp; | &nbsp;Services&nbsp; | &nbsp;Repair&nbsp; | &nbsp;Support&nbsp; | &nbsp;Contact</nav>
<div class="copyright abs">© 2014 Company Name&nbsp; All right reserved&nbsp; Term of Use</div>
<div class="social abs" style="left:883px;background:#5ab2e6" aria-label="Social link"></div>
<div class="social abs" style="left:910px;background:#1a6aa8" aria-label="Social link"></div>

</body>
</html>
```